Government Contracting business needs a website design.

Brisco & Wendell, LLC is a minority owned Service Disabled Veteran Owned Small Business (SDVOSB) that provides Strategic Planning, Public Health Emergency Response, and Data Management Solutions for Federal Civilian and Defense Agencies. We have over 20 years of experience helping health and defense agencies develop concept of operations, deploy assets and personnel in Hot Zones around the world, and deliver goods and services all of the globe.

We are a leader in the field of Data Management. We help our customers develop cloud migration and disaster recovery strategies. We are experts with database management, data replication, queries, consolidation, and records management.

We are looking for a very nice and simple website designs that states clearly what we do as a company and that is easy for our customers to follow. We would like to have some moving pictures that are base on our expertise. We want the website to be easy to use and have the scroll down features that keeps things all on the same page when clicking on the menu. I attached a document with what we need on the website. I will also attach our logo. We want it to look simple clean and very professional.

Target Market(s)

Government Contracting, Management Consulting, Health

Industry/Entity Type

Government

Coding

Coded - Design and coding required

Number of Pages Required

1 page

Font styles to use
Serif

Requirements
Must have
• Very nice picture slides that speaks to our capabilities in Disaster Response, Strategic Planning, and Database Management. Slick look and design. Make sure SDVOSB Logo is right at the beginning of website as our customers is looking for that certification. Very nice colors that blend well with our logo.
Nice to have
• Very nice and slick colors that blends well with logo.
Should not have
• Basic website design that are weary on the eye. No bright colors, just simple colors that looks good with logo.

```html
<!DOCTYPE html>
<html lang="en">
<head>
<meta charset="utf-8">
<title>Brisco &amp; Wendell, LLC</title>
<link href="https://fonts.googleapis.com/css2?family=Poppins:wght@400;500;600&display=swap" rel="stylesheet">
<style>
:root{
  --red:#c00d0d;
  --ink:#1d1d1d;
  --text:#6b6b6b;
  --light:#f2f2f2;
  --line:#d6d6d6;
  --footer:#1f1f1f;
  --footer-text:#a8a8a8;
  --footer-head:#e8e8e8;
  --white:#ffffff;
}
*{box-sizing:border-box;margin:0;padding:0}
html,body{width:1200px;height:3593px;overflow:hidden}
body{font-family:"Poppins",sans-serif;color:var(--ink);background:var(--white);position:relative}
.abs{position:absolute}
.btn{position:absolute;background:var(--red);color:var(--white);font-size:15px;display:flex;align-items:center;justify-content:center}
.btn-pill{border-radius:22px}
.section-title{position:absolute;left:0;width:1200px;text-align:center;font-size:44px;font-weight:400;letter-spacing:2px}
.title-rule{position:absolute;left:450px;width:300px;height:2px;background:var(--line)}
.title-rule::after{content:"";position:absolute;left:120px;top:-1px;width:60px;height:4px;background:var(--red)}
.red-rule{position:absolute;width:120px;height:2px;background:var(--red)}
.photo{position:absolute}

/* header */
.site-header{position:absolute;left:0;top:0;width:1200px;height:108px}
.brand{left:84px;top:26px;display:flex;align-items:center;gap:10px;font-size:19px;font-weight:600;color:var(--red)}
.brand-dot{width:44px;height:44px;border-radius:50%;background:var(--red)}
.top-link{top:24px;font-size:14px;display:flex;align-items:center;gap:10px}
.contact-btn{left:970px;top:14px;width:144px;height:38px;font-size:15px}
.main-nav{position:absolute;top:70px;left:326px;width:790px;display:flex;justify-content:space-between;font-size:14px;font-weight:500}
.main-nav span.sep{color:var(--text)}

.hero{left:0;top:108px;width:1200px;height:592px;background:linear-gradient(180deg,#9fb6d1 0%,#c9d4de 40%,#6f8a4a 72%,#8a8f7a 100%)}

/* about */
.about-title{left:86px;top:762px;font-size:40px;font-weight:400;letter-spacing:2px}
.about-text{left:86px;top:850px;width:492px;font-size:13.5px;line-height:26px;color:var(--text);text-align:justify}

/* services */
.services{left:0;top:1220px;width:1200px;height:548px;background:var(--light)}
.service-card{position:absolute;top:1478px;width:236px;height:177px;border:1px solid var(--line);text-align:center}
.service-icon{position:absolute;left:68px;top:-52px;width:100px;height:100px;border-radius:50%;background:var(--white);border:1px solid var(--line);display:flex;align-items:center;justify-content:center}
.service-name{position:absolute;left:0;top:78px;width:100%;font-size:17px;line-height:30px;letter-spacing:2px;color:#444}
.service-card .btn{left:27px;top:158px;width:180px;height:40px}
.arrow{position:absolute;top:1552px}

/* why */
.why-title{left:623px;top:1865px;font-size:40px;font-weight:400;letter-spacing:2px}
.why-list{left:623px;top:1975px;width:491px;list-style:none;font-size:15px;line-height:31px;color:var(--text);text-align:justify}
.why-list li{margin-bottom:24px}
.why-list li::before{content:"•";color:var(--red);margin-right:22px;font-size:18px}

/* leadership */
.leader-name{font-size:18px;font-weight:500}
.leader-role{font-size:15px;color:var(--text);margin-top:6px}
.leader-bio{font-size:13.5px;line-height:23px;color:var(--text);margin-top:36px}
.leader-info{position:absolute;top:2553px;width:230px}
.leader-info::before{content:"";position:absolute;left:0;top:-8px;width:180px;height:1px;background:var(--line)}

/* testimonial */
.quote-band{left:0;top:3004px;width:1200px;height:128px;background:var(--red)}
.quote-text{left:0;top:3076px;width:1200px;text-align:center;color:var(--white);font-size:18px}
.avatar{left:534px;top:2918px;width:128px;height:128px;border-radius:50%;border:5px solid var(--white);background:linear-gradient(160deg,#b49a84,#6b5a4e)}

/* footer */
.site-footer{left:0;top:3132px;width:1200px;height:461px;background:var(--footer)}
.footer-brand{left:84px;top:3206px;width:246px;display:flex;justify-content:center;align-items:center;gap:10px;font-size:18px;font-weight:600;color:var(--red)}
.footer-brand span.dot{width:36px;height:36px;border-radius:50%;background:var(--red)}
.contact-line{position:absolute;left:86px;width:280px;font-size:14px;line-height:24px;display:flex;gap:14px;padding-bottom:16px;color:var(--footer-text)}
.contact-line.ruled{border-bottom:1px solid #3a3a3a}
.footer-head{font-size:16px;color:var(--footer-head)}
.footer-links{left:518px;top:3262px;list-style:none;font-size:12px;letter-spacing:1px;color:var(--footer-text)}
.footer-links li{height:44px;display:flex;align-items:center;gap:14px}
.footer-links li::before{content:"";width:10px;height:10px;border-radius:50%;border:1px solid #666}
.newsletter-note{left:824px;top:3268px;width:290px;font-size:13px;line-height:24px;color:var(--footer-text)}
.email-field{left:824px;top:3348px;width:288px;height:46px;border:1px solid #666;font-size:13px;padding-left:16px;display:flex;align-items:center;color:var(--footer-text)}
.copyright{left:0;top:3535px;width:1200px;border-top:1px solid #3a3a3a;padding-top:16px;text-align:center;font-size:12px;color:#7a7a7a}
</style>
</head>
<body>

<header class="site-header">
  <div class="abs brand"><span class="brand-dot"></span>Brisco &amp; Wendell</div>
  <div class="abs top-link" style="left:708px">
    <svg width="12" height="14" viewBox="0 0 12 14"><rect x="1" y="6" width="10" height="8" fill="#c00d0d"/><path d="M3 6V4a3 3 0 0 1 6 0v2" stroke="#c00d0d" stroke-width="2" fill="none"/></svg>Login</div>
  <div class="abs top-link" style="left:818px">
    <svg width="14" height="14" viewBox="0 0 14 14"><rect x="1" y="3" width="10" height="10" fill="none" stroke="#c00d0d" stroke-width="1.6"/><path d="M5 9l7-7" stroke="#c00d0d" stroke-width="2"/></svg>Registration</div>
  <div class="btn contact-btn">Contact Us</div>
  <nav class="main-nav">
    <span>About Us</span><span class="sep">|</span><span>Team</span><span class="sep">|</span><span>Core Capabilities</span><span class="sep">|</span><span>Agencies We Serve</span><span class="sep">|</span><span>Contact us</span>
  </nav>
</header>

<div class="abs hero" role="img" aria-label="Park path with blossoming trees and a tall evergreen under a cloudy sky"></div>

<section id="about">
  <h2 class="abs about-title">About Us</h2>
  <div class="red-rule" style="left:86px;top:824px"></div>
  <p class="abs about-text">Brisco &amp; Wendell, LLC is a minority owned Service Disabled Veteran Owned Small Business (SDVOSB) that provides Strategic Planning, Public Health Emergency Response, and Data Management Solutions for Federal Civilian and Defense Agencies. We have over 20 years of experience helping health and defense agencies develop concept of operations, deploy assets and personnel in Hot Zones around the world, and deliver goods and services all of the globe.</p>
  <div class="btn" style="left:86px;top:1085px;width:136px;height:48px">LEARN MORE</div>
  <div class="photo" style="left:634px;top:774px;width:480px;height:358px;background:linear-gradient(180deg,#a9b8c6 0%,#6f7b5c 50%,#5d4b3a 100%)" role="img" aria-label="Lakeside park with bare trees and open ground"></div>
</section>

<section id="services">
  <div class="abs services"></div>
  <h2 class="section-title" style="top:1282px">Our Services</h2>
  <div class="title-rule" style="top:1356px"></div>
  <svg class="arrow" style="left:28px" width="24" height="40" viewBox="0 0 24 40"><path d="M20 2L4 20l16 18" stroke="#bbb" stroke-width="2" fill="none"/></svg>
  <svg class="arrow" style="left:1146px" width="24" height="40" viewBox="0 0 24 40"><path d="M4 2l16 18L4 38" stroke="#bbb" stroke-width="2" fill="none"/></svg>

  <div class="service-card" style="left:86px">
    <div class="service-icon"><svg width="44" height="44" viewBox="0 0 44 44"><path d="M6 38h32M6 6v32" stroke="#777" stroke-width="3" fill="none"/><path d="M14 30l18-18 4 4-18 18h-4z" fill="#777"/></svg></div>
    <div class="service-name">STRATEGIC<br>PLANNING</div>
    <div class="btn btn-pill">LEARN MORE</div>
  </div>
  <div class="service-card" style="left:348px">
    <div class="service-icon"><svg width="44" height="44" viewBox="0 0 44 44"><rect x="6" y="28" width="6" height="10" fill="#777"/><rect x="16" y="22" width="6" height="16" fill="#777"/><rect x="26" y="16" width="6" height="22" fill="#777"/><path d="M6 22l10-8 8 4 14-12" stroke="#777" stroke-width="3" fill="none"/></svg></div>
    <div class="service-name">PUBLIC HEALTH<br>EMERGENCY....</div>
    <div class="btn btn-pill">LEARN MORE</div>
  </div>
  <div class="service-card" style="left:612px">
    <div class="service-icon"><svg width="44" height="44" viewBox="0 0 44 44"><path d="M22 4l15 6v10c0 10-7 17-15 20C14 37 7 30 7 20V10z" fill="#777"/><path d="M15 22l5 5 9-10" stroke="#fff" stroke-width="3" fill="none"/></svg></div>
    <div class="service-name">DATA MANAGEMENT<br>SERVICES</div>
    <div class="btn btn-pill">LEARN MORE</div>
  </div>
  <div class="service-card" style="left:877px">
    <div class="service-icon"><svg width="44" height="44" viewBox="0 0 44 44"><circle cx="14" cy="8" r="4" stroke="#777" stroke-width="3" fill="none"/><circle cx="30" cy="8" r="4" stroke="#777" stroke-width="3" fill="none"/><circle cx="14" cy="36" r="4" stroke="#777" stroke-width="3" fill="none"/><path d="M14 12v20M30 12c0 12-16 8-16 20" stroke="#777" stroke-width="3" fill="none"/></svg></div>
    <div class="service-name">CONTRACTS<br>VEHICLES</div>
    <div class="btn btn-pill">LEARN MORE</div>
  </div>
</section>

<section id="why">
  <div class="photo" style="left:84px;top:1870px;width:482px;height:372px;background:linear-gradient(180deg,#b3c1cf 0%,#5f6f4f 52%,#4f3f30 100%)" role="img" aria-label="Park by a lake with bare trees at dusk"></div>
  <h2 class="abs why-title">Why Hire Us?</h2>
  <div class="red-rule" style="left:623px;top:1928px"></div>
  <ul class="abs why-list">
    <li>Over 20 years of experience deploying assets and personnel to disaster zones around the US and the world.</li>
    <li>Over 20 years of experience developing concept of operations and stakeholder management strategies for Federal Agencies.</li>
  </ul>
  <div class="btn" style="left:623px;top:2192px;width:137px;height:48px">Learn More</div>
</section>

<section id="team">
  <h2 class="section-title" style="top:2378px">Leadership Team</h2>
  <div class="title-rule" style="top:2453px"></div>

  <div class="photo" style="left:86px;top:2528px;width:234px;height:258px;background:linear-gradient(160deg,#d8dde2,#2b3340)" role="img" aria-label="Portrait of the chief executive"></div>
  <div class="leader-info" style="left:346px">
    <div class="leader-name">Ret. SFC Dalton R. Brisco</div>
    <div class="leader-role">Chief Executive Office</div>
    <p class="leader-bio">Brisco &amp; Wendell, LLC was founded by Retired Sergeant First Class (Ret. SFC) Dalton Brisco.</p>
  </div>
  <div class="btn btn-pill" style="left:346px;top:2745px;width:138px;height:40px">Learn More</div>

  <div class="photo" style="left:624px;top:2528px;width:234px;height:258px;background:linear-gradient(160deg,#4a3a2e,#1d1d22)" role="img" aria-label="Portrait of the executive partner"></div>
  <div class="leader-info" style="left:884px">
    <div class="leader-name">Mr. Vincent T. Wendell</div>
    <div class="leader-role">Chief Executive Office</div>
    <p class="leader-bio">Brisco &amp; Wendell, LLC was founded by Retired Sergeant First Class (Ret. SFC) Dalton Brisco.</p>
  </div>
  <div class="btn btn-pill" style="left:884px;top:2745px;width:138px;height:40px">Learn More</div>
</section>

<section id="testimonial">
  <div class="abs quote-band"></div>
  <div class="abs avatar" role="img" aria-label="Portrait of the business owner"></div>
  <p class="abs quote-text">Lorem Ipsum is simply dummy text of the printing and typesetting industry.&nbsp; Simply dummy.&nbsp; ~ Mara Ellison, owner</p>
</section>

<footer class="abs site-footer"></footer>
<div class="abs footer-brand"><span class="dot"></span>Brisco &amp; Wendell</div>
<div class="contact-line ruled" style="top:3308px">
  <svg width="14" height="18" viewBox="0 0 14 18" style="flex:none;margin-top:4px"><path d="M7 1a6 6 0 0 1 6 6c0 4-6 10-6 10S1 11 1 7a6 6 0 0 1 6-6z" fill="none" stroke="#888" stroke-width="1.5"/><circle cx="7" cy="7" r="2" fill="#888"/></svg>
  <span>12th Floor, 400 Meridian Plaza<br>Riverside District RD4 7QA</span></div>
<div class="contact-line ruled" style="top:3393px">
  <svg width="14" height="14" viewBox="0 0 14 14" style="flex:none;margin-top:5px"><path d="M2 1h3l1 3-2 1a8 8 0 0 0 5 5l1-2 3 1v3c-7 1-12-4-11-11z" fill="none" stroke="#888" stroke-width="1.4"/></svg>
  <span>Telephone : 07440115274</span></div>
<div class="contact-line" style="top:3443px">
  <svg width="16" height="12" viewBox="0 0 16 12" style="flex:none;margin-top:6px"><rect x="1" y="1" width="14" height="10" fill="none" stroke="#888" stroke-width="1.4"/><path d="M1 1l7 6 7-6" fill="none" stroke="#888" stroke-width="1.4"/></svg>
  <span>Email : info@briscowendell.com</span></div>

<div class="abs footer-head" style="left:518px;top:3210px">Our company</div>
<ul class="abs footer-links">
  <li>HOME</li><li>ABOUT US</li><li>OUR PROJECTS</li><li>PROPERTY PROJECTS</li><li>CONTACT</li>
</ul>

<div class="abs footer-head" style="left:824px;top:3212px">Sign up to newsletter</div>
<p class="abs newsletter-note">You may unsubscribe at any moment. For that purpose, the legal notice.</p>
<div class="abs email-field">Enter Your Email ID...</div>
<div class="btn" style="left:824px;top:3414px;width:130px;height:42px">Subscribe</div>

<div class="abs copyright">© 2017 Brisco &amp; Wendell - All Rights Reserved</div>

</body>
</html>
```